Silver Ridge Business Card Design

I have an existing corporate logo. I'd like to clean it up bit (sharpen it up) and make it look better (without major redesign). I'd like to get the logo itself in all major file formats for print, web, etc.
Then I'd like a business card design that reflects a strategy consulting firm. It should be clean - logo and text without major graphics, and perhaps some small color treatments that match the logo color. The card should suggest high quality in terms of the company.
I'd like the files for card in all major print formats.
Target Market(s)
Silver Ridge Partners is a strategy development and business consulting firm focused on small to mid-sized companies. We specialize in business strategy, comprehensive business plan development, market segmentation and positioning, financial models, marketing and sales strategy, product strategy and the effective use of social media in business growth. We operate as consultants, advisers, retained members of management teams, and Board members. We often serve in the role of Chief Strategy Officer, supporting CEO's and other senior executives to enhance top and bottom line growth.
Our overall approach with clients is to deliver actual results, and we often take an active team role with business founders and management teams to drive business growth and affect real changes in performance. As a result, we approach each situation uniquely and partner with clients in a manner that will have the biggest impact on enterprise value.
Business
Look and feel

```html
<!DOCTYPE html>
<html lang="en">
<head>
<meta charset="utf-8">
<title>Silver Ridge Partners – Business Card</title>
<link rel="stylesheet" href="https://fonts.googleapis.com/css2?family=Exo+2:wght@400;600&display=swap">
<style>
  :root {
    --page-bg: #e9e8e6;
    --panel-light-a: #f5f5f6;
    --panel-light-b: #d9dadd;
    --panel-dark: #3b3b3d;
    --accent-navy: #2f3f74;
    --text-light: #f1f1f1;
    --text-muted: #d4d4d6;
  }
  * { margin: 0; padding: 0; box-sizing: border-box; }
  html, body {
    width: 1200px; height: 768px; overflow: hidden;
    background: var(--page-bg);
    font-family: "Exo 2", sans-serif;
  }
  .card {
    position: absolute; left: 100px; top: 96px;
    width: 1000px; height: 575px;
    box-shadow: 0 14px 40px rgba(0,0,0,0.18);
  }
  .card-shapes { position: absolute; inset: 0; width: 100%; height: 100%; }
  .brand {
    position: absolute; left: 120px; top: 248px;
    display: flex; align-items: center; gap: 16px;
  }
  .brand-dot {
    width: 34px; height: 34px; border-radius: 50%;
    background: var(--accent-navy); flex: none;
  }
  .brand-name {
    color: var(--accent-navy); font-weight: 600;
    font-size: 31px; line-height: 1.12; letter-spacing: 1.5px;
    text-transform: uppercase;
  }
  .person { position: absolute; left: 665px; top: 92px; color: var(--text-light); }
  .person-name { font-size: 28px; font-weight: 400; letter-spacing: 0.5px; }
  .person-role { font-size: 18px; color: var(--text-muted); margin-top: 2px; }
  .address {
    position: absolute; left: 665px; top: 248px;
    font-size: 18px; line-height: 1.45; color: var(--text-light);
  }
  .contact-list {
    position: absolute; left: 665px; top: 385px;
    list-style: none; color: var(--text-light); font-size: 16.5px;
  }
  .contact-list li { display: flex; align-items: center; gap: 12px; height: 28px; }
  .contact-icon { width: 15px; height: 15px; fill: var(--text-light); flex: none; }
</style>
</head>
<body>
  <section class="card" aria-label="Silver Ridge Partners business card">
    <svg class="card-shapes" viewBox="0 0 1000 575" preserveAspectRatio="none" aria-hidden="true">
      <defs>
        <linearGradient id="light-panel" x1="0" y1="0" x2="1" y2="1">
          <stop offset="0" stop-color="var(--panel-light-a)"/>
          <stop offset="1" stop-color="var(--panel-light-b)"/>
        </linearGradient>
      </defs>
      <rect width="1000" height="575" fill="url(#light-panel)"/>
      <path d="M520 0 Q610 290 548 575 L600 575 Q665 290 548 0 Z" fill="var(--accent-navy)"/>
      <path d="M548 0 Q665 290 600 575 L1000 575 L1000 0 Z" fill="var(--panel-dark)"/>
    </svg>

    <div class="brand">
      <span class="brand-dot"></span>
      <span class="brand-name">Silver Ridge<br>Partners, LLC</span>
    </div>

    <div class="person">
      <div class="person-name">Maren Holt-Avery</div>
      <div class="person-role">consultant</div>
    </div>

    <address class="address" style="font-style:normal">214.9th floor,Quarry Lane<br>Road NRT</address>

    <ul class="contact-list">
      <li>
        <svg class="contact-icon" viewBox="0 0 16 16" aria-label="Phone"><path d="M3.5 1l3 3-1.6 1.8c.8 1.9 2.4 3.5 4.3 4.3L11 8.5l3 3-2 2.5C6.5 13.5 2.5 9.5 1 4z"/></svg>
        012 555 0147
      </li>
      <li>
        <svg class="contact-icon" viewBox="0 0 16 16" aria-label="Mobile"><path d="M4.5 0h7a1 1 0 0 1 1 1v14a1 1 0 0 1-1 1h-7a1 1 0 0 1-1-1V1a1 1 0 0 1 1-1zm.8 2v10h5.4V2zM8 13a1 1 0 1 0 0 2 1 1 0 0 0 0-2z"/></svg>
        012 555 0148
      </li>
      <li>
        <svg class="contact-icon" viewBox="0 0 16 16" aria-label="Fax"><path d="M4 1h8v4H4zM1 6h14v7h-3v2H4v-2H1zm4 5v3h6v-3z"/></svg>
        012 555 0149
      </li>
      <li>
        <svg class="contact-icon" viewBox="0 0 16 16" aria-label="Email"><path d="M1 3h14v10H1zm1.5 1.3L8 8.5l5.5-4.2z"/></svg>
        maren@srpmail.com
      </li>
      <li>
        <svg class="contact-icon" viewBox="0 0 16 16" aria-label="Website"><path d="M8 1a7 7 0 1 0 0 14A7 7 0 0 0 8 1zm0 1.5c.8 0 1.7 1.6 2 4H6c.3-2.4 1.2-4 2-4zM2.6 6.5h2c-.1.5-.1 1-.1 1.5s0 1 .1 1.5h-2a5.5 5.5 0 0 1 0-3zm3.4 3h4c-.3 2.4-1.2 4-2 4s-1.7-1.6-2-4zm5.4 0c.1-.5.1-1 .1-1.5s0-1-.1-1.5h2a5.5 5.5 0 0 1 0 3z"/></svg>
        www.srpartners.com
      </li>
    </ul>
  </section>
</body>
</html>
```